New Business Card Design Project

The look of the business cards should include
-Clean Lines
-Should suit a sophisticated customer
-Evoke a mix of business and creativity
-Incorporate the color Gray or Black:White palette
-Open to see layouts in both vertical and horizontal
3 partners (we need 3 cards)
NORELLE VASK
ODA TRENCHARD
MARU ELDFORTH
Reason: We would like more submissions please
Target Market(s)
We are a NYC and European based boutique consulting agency specializing in fashion business and creative clients. In addition to consulting we will be offering an e-commerce site selling women’s accessories and jewelry geared towards fashion forward women ages 25-50.
Industry/Entity Type
Business
Font styles to use
Requirements
Must have
- - texture
- grayscale
3 Partners
Details for each card
CONSULTING I DESIGN
MARU ELDFORTH
Founding Partner
917.555.0183
maru@theplumwickhouse.com
www.theplumwickhouse.com
CONSULTING I DESIGN
NORELLE VASK
Founding Partner
917.555.0147
norelle@theplumwickhouse.com
www.theplumwickhouse.com
CONSULTING I DESIGN
Oda Kestlin Trenchard
Founding Partner
(no phone for her)
Oda@theplumwickhouse.com
www.theplumwickhouse.com

```html
<!DOCTYPE html>
<html lang="en">
<head>
<meta charset="utf-8">
<title>The Plumwick House — Business Cards</title>
<link rel="stylesheet" href="https://fonts.googleapis.com/css2?family=Arimo:wght@400&family=Questrial&display=swap">
<style>
  :root {
    --backdrop: #e9e9e9;
    --card: #333333;
    --ink: #ffffff;
    --ink-soft: #d8d8d8;
    --divider: rgba(255, 255, 255, 0.06);
  }
  * { margin: 0; padding: 0; box-sizing: border-box; }
  html, body {
    width: 1200px;
    height: 782px;
    overflow: hidden;
    background: var(--backdrop);
  }
  .stage {
    position: relative;
    width: 1200px;
    height: 782px;
  }
  .card {
    position: absolute;
    background: var(--card);
    box-shadow: 0 2px 6px rgba(0, 0, 0, 0.18);
    color: var(--ink);
  }

  /* Horizontal front */
  .card--front {
    left: 138px;
    top: 340px;
    width: 550px;
    height: 310px;
  }
  .card__fold {
    position: absolute;
    left: 292px;
    top: 0;
    width: 1px;
    height: 100%;
    background: var(--divider);
  }
  .contact {
    position: absolute;
    left: 62px;
    top: 114px;
    font-family: "Arimo", Arial, sans-serif;
  }
  .contact__name {
    font-size: 14px;
    letter-spacing: 0.2px;
    line-height: 16px;
  }
  .contact__role {
    font-size: 11px;
    letter-spacing: 0.6px;
    color: var(--ink-soft);
    margin-top: 2px;
    margin-bottom: 10px;
  }
  .contact__line {
    display: flex;
    align-items: center;
    font-size: 13px;
    height: 21px;
    white-space: nowrap;
  }
  .contact__icon {
    width: 27px;
    flex: none;
    display: flex;
    justify-content: flex-start;
    padding-left: 4px;
  }
  .contact__icon--mail { padding-left: 0; }

  /* Brand name: single line, plain, with one small circle */
  .brand {
    position: absolute;
    display: flex;
    align-items: center;
    justify-content: center;
    gap: 10px;
    font-family: "Questrial", Helvetica, sans-serif;
    color: var(--ink);
    white-space: nowrap;
  }
  .brand__dot {
    width: 9px;
    height: 9px;
    border-radius: 50%;
    background: var(--ink);
    flex: none;
  }
  .brand__name {
    font-size: 21px;
    letter-spacing: 0.5px;
    line-height: 28px;
  }
  .card--front .brand {
    left: 293px;
    top: 136px;
    width: 257px;
    height: 28px;
  }
  .tagline {
    position: absolute;
    left: 296px;
    top: 236px;
    width: 216px;
    text-align: center;
    font-family: "Questrial", Helvetica, sans-serif;
    font-size: 9px;
    letter-spacing: 2.6px;
  }

  /* Vertical back */
  .card--back {
    left: 711px;
    top: 84px;
    width: 328px;
    height: 570px;
  }
  .rotated {
    position: absolute;
    transform-origin: center center;
    transform: translate(-50%, -50%) rotate(90deg);
  }
  .card--back .web {
    left: 55px;
    top: 284px;
    font-family: "Arimo", Arial, sans-serif;
    font-size: 11px;
    letter-spacing: 1.3px;
    white-space: nowrap;
  }
  .card--back .brand {
    left: 164px;
    top: 284px;
    width: 230px;
    height: 28px;
  }
</style>
</head>
<body>
<main class="stage">

  <section class="card card--front" aria-label="Business card, front">
    <div class="card__fold"></div>

    <div class="contact">
      <p class="contact__name">MARU ELDFORTH</p>
      <p class="contact__role">Founding Partner</p>
      <p class="contact__line">
        <span class="contact__icon">
          <svg width="10" height="16" viewBox="0 0 10 16" aria-hidden="true">
            <rect x="1" y="0.75" width="8" height="14.5" rx="1.2" fill="none" stroke="#fff" stroke-width="1.3"/>
            <rect x="2.6" y="2.6" width="4.8" height="7.2" fill="#fff"/>
            <circle cx="5" cy="12.6" r="0.9" fill="#fff"/>
          </svg>
        </span>
        917.555.0183
      </p>
      <p class="contact__line">
        <span class="contact__icon contact__icon--mail">
          <svg width="20" height="12" viewBox="0 0 20 12" aria-hidden="true">
            <rect x="0.5" y="0.5" width="19" height="11" fill="#fff"/>
            <path d="M1 1 L10 7 L19 1" fill="none" stroke="#333" stroke-width="1.3"/>
            <path d="M1 11 L7.5 5.5 M19 11 L12.5 5.5" fill="none" stroke="#333" stroke-width="1"/>
          </svg>
        </span>
        maru@theplumwickhouse.com
      </p>
    </div>

    <div class="brand">
      <span class="brand__dot"></span>
      <p class="brand__name">The Plumwick House</p>
    </div>

    <p class="tagline">CONSULTING I DESIGN</p>
  </section>

  <section class="card card--back" aria-label="Business card, back">
    <p class="web rotated">www.theplumwickhouse.com</p>
    <div class="brand rotated">
      <span class="brand__dot"></span>
      <p class="brand__name">The Plumwick House</p>
    </div>
  </section>

</main>
</body>
</html>
```